Dental Services Conceirge Business Card Design

I need two sided business card for Rudy who helps dental patients navigate the city with dental appointments, xray appointments, hotels, transportation, ect. The target user are dental paitents for Lira Dental. http://pelutomarvendds.example/ Rudy does not work for Lira Dental so they should not be on the card. Rudy typically stands outside the dental office and helps either customers or visitors walking by.
One side I'd like his photo, name, title address and phone (see attached for photo)
Name: Rudy Benhart. His "street name" is Rudy so you can emphasize his first name.
Title: Dental Services Concierge.
Address and phone:
38 "K" Ave. & Ninth St.
Villa Corvana, B.C.
USA: (555) 304 6187
MX: 011-526-555-207-913
On the back I would like a map that indicate where you can find RUdy outside the dental office. This should include where the US border is. I attached an example.
Target Market(s)
Elderly people needing dental services
Industry/Entity Type
Business
Contact Information for Business Card
Need front and back business card. name and contact info on the front and a map on the back
Font styles to use
Look and feel
Each slider illustrates characteristics of the customer's brand and the style your logo design should communicate.

```html
<!DOCTYPE html>
<html lang="en">
<head>
<meta charset="utf-8">
<title>Rudy Benhart – Dental Services Concierge</title>
<link rel="stylesheet" href="https://fonts.googleapis.com/css2?family=Salsa&family=Roboto:wght@400&display=swap">
<style>
  :root {
    --page-bg: #e4e2de;
    --card-bg: #f1f2f1;
    --teal: #1c6f86;
    --red: #d62a22;
    --navy: #2b3a78;
    --ink: #1b1b1b;
    --phone: #c6a574;
    --photo-a: #b7b2aa;
    --photo-mid: #8a7e74;
    --photo-b: #3b4a7a;
  }
  * { margin: 0; padding: 0; box-sizing: border-box; }
  html, body { width: 1200px; height: 1054px; overflow: hidden; background: var(--page-bg); }
  .card {
    position: absolute; left: 100px; top: 224px;
    width: 1000px; height: 605px;
    background: var(--card-bg);
    overflow: hidden;
    box-shadow: 0 6px 24px rgba(0,0,0,.18);
  }
  .card-art { position: absolute; inset: 0; }
  .card-name {
    position: absolute; right: 60px; top: 66px;
    font-family: "Salsa", cursive; font-weight: 400; font-size: 44px; color: var(--teal);
    line-height: 1; white-space: nowrap;
  }
  .card-title {
    position: absolute; right: 60px; top: 126px;
    font-family: "Roboto", sans-serif; font-size: 29px; color: var(--ink); white-space: nowrap;
  }
  .card-address {
    position: absolute; right: 60px; top: 196px; text-align: right;
    font-family: "Roboto", sans-serif; font-size: 24px; line-height: 37px; color: var(--ink); white-space: nowrap;
  }
  .card-phones {
    position: absolute; right: 60px; top: 462px; list-style: none;
    font-family: "Roboto", sans-serif; font-size: 26px; color: var(--phone);
  }
  .card-phones li { display: flex; align-items: center; justify-content: flex-end; height: 40px; white-space: nowrap; }
  .country-mark { width: 38px; height: 20px; margin-left: 16px; display: block; }
</style>
</head>
<body>
  <div class="card">
    <svg class="card-art" width="1000" height="605" viewBox="0 0 1000 605">
      <defs>
        <linearGradient id="portraitTone" x1="0" y1="0" x2="1" y2="1">
          <stop offset="0" stop-color="var(--photo-a)"/>
          <stop offset="0.6" stop-color="var(--photo-mid)"/>
          <stop offset="1" stop-color="var(--photo-b)"/>
        </linearGradient>
        <linearGradient id="portraitFade" x1="0" y1="0" x2="1" y2="0">
          <stop offset="0.55" stop-color="#fff"/>
          <stop offset="1" stop-color="#000"/>
        </linearGradient>
        <mask id="portraitMask"><rect x="0" y="0" width="560" height="605" fill="url(#portraitFade)"/></mask>
      </defs>
      <rect class="portrait" x="0" y="30" width="560" height="575" fill="url(#portraitTone)" mask="url(#portraitMask)"
            role="img" aria-label="Portrait photo of Rudy Benhart in a navy scrub top"/>
      <path class="wave-teal" d="M0,545 C250,600 520,520 720,420 C820,370 900,348 1000,350 L1000,605 L0,605 Z" fill="var(--teal)"/>
      <path class="wave-navy" d="M0,500 C220,575 470,575 660,470 L665,478 C470,590 220,590 0,530 Z" fill="var(--navy)" opacity=".9"/>
      <path class="wave-red" d="M0,470 C220,545 480,540 680,420 C800,350 900,318 1000,316 L1000,334 C900,336 810,368 690,438 C490,560 220,565 0,494 Z" fill="var(--red)"/>
      <path class="wave-red-thin" d="M0,540 C220,600 450,600 600,510 L604,516 C450,612 220,612 0,552 Z" fill="var(--red)"/>
    </svg>

    <h1 class="card-name">Rudy Benhart</h1>
    <p class="card-title">Dental Services Concierge</p>
    <p class="card-address">38 "K" Ave. &amp; Ninth St.<br>Villa Corvana, B.C.</p>
    <ul class="card-phones">
      <li>(555) 304 6187
        <svg class="country-mark" viewBox="0 0 38 20" role="img" aria-label="USA">
          <rect width="38" height="20" fill="#b8323a"/>
          <rect y="3" width="38" height="3" fill="#fff"/><rect y="9" width="38" height="3" fill="#fff"/><rect y="15" width="38" height="3" fill="#fff"/>
          <rect width="16" height="11" fill="#2f3d7a"/>
        </svg>
      </li>
      <li>011-526-555-207-913
        <svg class="country-mark" viewBox="0 0 38 20" role="img" aria-label="Mexico">
          <rect width="13" height="20" fill="#1f7a45"/><rect x="13" width="12" height="20" fill="#fff"/><rect x="25" width="13" height="20" fill="#c8312f"/>
        </svg>
      </li>
    </ul>
  </div>
</body>
</html>
```